German Webagency needs fresh modern Design

Our website is 4 years old. We need an fresh modern website. All pics we used before are from customers or handmade by us. the new website should be clear with nice handling. please dont copy something from template websites. it would be great if you can surprise us with something great. its our first project here. don´t worry if i make a mistake in responding or briefing. after 20 years you can´t see the works of your own "designer" so we hope for help :-)
our existing site: www.tovankreativ.de
Target Market(s)
small and middle sized companys in germany
Number of Pages Required
4 page
Font styles to use
Colors
Designer to choose colors to be used in the design.
Requirements
Must have
- Responsive (sure we code it)
- Modern and big Font ..Headlines and Slider
- innovative..if you know something new..feel free to show
Nice to have
- the site with our works/refences should look great and later easy to handle when we code it or use wp.
- we like black and grey but if you have better ideas also feel free
Should not have
- a cup of coffe..laptop.. a pencil a handwritten font
- dont copy and modify templates from know websites..bad style

```html
<!DOCTYPE html>
<html lang="de">
<head>
<meta charset="utf-8">
<title>tovankreativ.de – Webagentur</title>
<link rel="stylesheet" href="https://fonts.googleapis.com/css2?family=Jost:wght@500;600;700&display=swap">
<style>
  :root {
    --night: #02020f;
    --texture: #1d2338;
    --texture-light: #2a3350;
    --white: #ffffff;
    --accent: #3f69b3;
  }
  * { box-sizing: border-box; margin: 0; padding: 0; }
  html, body { width: 1200px; height: 750px; overflow: hidden; background: var(--night); }
  .hero {
    position: relative;
    width: 1200px;
    height: 750px;
    overflow: hidden;
    font-family: "Jost", "Futura", sans-serif;
    color: var(--white);
  }
  .hero__backdrop { position: absolute; inset: 0; width: 100%; height: 100%; }
  .site-header {
    position: absolute;
    top: 74px;
    left: 150px;
    display: flex;
    align-items: center;
  }
  .brand {
    font-weight: 700;
    font-size: 17px;
    color: var(--white);
    text-decoration: none;
    letter-spacing: 0.01em;
    margin-right: 50px;
  }
  .main-nav { display: flex; gap: 50px; }
  .main-nav a {
    color: var(--white);
    text-decoration: none;
    font-weight: 600;
    font-size: 13.5px;
  }
  .headline {
    position: absolute;
    left: 151px;
    top: 170px;
    font-weight: 700;
    font-size: 88px;
    line-height: 92px;
    letter-spacing: 0.115em;
    text-transform: uppercase;
    white-space: nowrap;
  }
  .headline span { display: block; }
  .headline .accent { color: var(--accent); }
  .cta {
    position: absolute;
    left: 156px;
    top: 602px;
    width: 242px;
    height: 63px;
    background: var(--accent);
    color: var(--white);
    display: flex;
    align-items: center;
    justify-content: center;
    font-weight: 700;
    font-size: 28px;
    letter-spacing: 0.1em;
    text-decoration: none;
  }
</style>
</head>
<body>
<main class="hero">
  <svg class="hero__backdrop" viewBox="0 0 1200 750" role="img" aria-label="Feine diagonale Linienstruktur um eine dunkle, geschwungene Fläche">
    <defs>
      <linearGradient id="textureTone" x1="0" y1="0" x2="1" y2="1">
        <stop offset="0" stop-color="var(--texture-light)"/>
        <stop offset="0.5" stop-color="var(--texture)"/>
        <stop offset="1" stop-color="var(--texture-light)"/>
      </linearGradient>
    </defs>
    <rect width="1200" height="750" fill="url(#textureTone)"/>
    <path fill="var(--night)" d="M530 0 C380 20 200 90 125 200 C65 290 60 430 0 525 L0 750 L700 750 C800 640 960 600 1060 480 C1150 370 1110 180 1142 0 Z"/>
  </svg>

  <header class="site-header">
    <a class="brand" href="#">tovankreativ.de</a>
    <nav class="main-nav">
      <a href="#">Über Uns</a>
      <a href="#">Services</a>
      <a href="#">Referenzen</a>
      <a href="#">Kontakt</a>
    </nav>
  </header>

  <h1 class="headline">
    <span>Nicht einfach</span>
    <span>perfekte Seiten,</span>
    <span class="accent">wir optimieren</span>
    <span class="accent">ihr Geschäft</span>
  </h1>

  <a class="cta" href="#">KONTAKT</a>
</main>
</body>
</html>
```